Web Design - 1 page for Buy - Repair - Service - Upgrade - PC Maintenance

We specialize in consumer and small business. It will be mobile friendly, viewable on all devices. Fully editable at the text level of the sections !!! - HTML / CSS only to be able to add a section would be to the web site
Updates

Target Market(s)

consumer and small business IT.

Coding

Coded - Design and coding required

Number of Pages Required

1 page

Font styles to use
Sans Serif

Requirements
Must have
• Looking for a page with a design that compliments the business card and pamphlet that has already been made (attached files). It should look professional and easy to read business. Email and phone number should be visible when the page loads. I do not want any forms for people to mess with. No "Contact Us" form or enter in email for newsletter. Customers will just be looking for this site to confirm we are professionals and have our business in order. OpenStreetMap: embedding map in webpage (like Google Maps) to where the workshop is located
Nice to have
• 2vask.com => this style of website would be more modern visually by integrating higher demands

```html
<!DOCTYPE html>
<html lang="en">
<head>
<meta charset="utf-8">
<title>Norvale Tech – Buy, Repair, Service, Upgrade</title>
<link rel="stylesheet" href="https://fonts.googleapis.com/css2?family=Open+Sans:wght@400;600;700;800&display=swap">
<style>
  :root{
    --blue:#2f86c9;
    --blue-deep:#1f6fb2;
    --ink:#2b2b2b;
    --text:#6d6d6d;
    --footer:#1b1b1b;
    --white:#ffffff;
  }
  *{box-sizing:border-box;margin:0;padding:0}
  html,body{width:1200px;height:4928px;overflow:hidden}
  body{font-family:"Open Sans",Arial,sans-serif;background:var(--white);color:var(--text);position:relative}

  /* top bar */
  .topbar{height:80px;display:flex;align-items:center;padding:0 40px;background:var(--white)}
  .brand{display:flex;align-items:center;gap:12px;font-weight:800;font-size:26px;color:var(--blue-deep);letter-spacing:1px;white-space:nowrap}
  .brand-dot{width:22px;height:22px;background:var(--blue);border-radius:50%;flex:none}
  .topbar-contact{margin-left:auto;display:flex;gap:60px;font-size:15px;color:var(--text)}
  .topbar-contact span{display:flex;align-items:center;gap:10px}
  .topbar-contact svg{width:18px;height:18px;fill:var(--blue)}

  /* hero */
  .hero{height:450px;display:flex}
  .hero-menu{width:470px;background:linear-gradient(160deg,#3e97d8,#1f6fb2);padding:130px 0 0 80px}
  .hero-menu li{list-style:none;color:var(--white);font-weight:700;font-size:26px;line-height:46px;display:flex;align-items:center;gap:18px;text-transform:uppercase;white-space:nowrap}
  .hero-menu li::before{content:"";width:18px;height:18px;border:2px solid var(--white);border-radius:50%;flex:none}
  .hero-photo{flex:1;background:linear-gradient(120deg,#e9edf0,#c8ccd0 55%,#8f959b)}

  /* intro */
  .intro{height:280px;padding:70px 120px 0;text-align:center}
  .intro h1{font-size:30px;font-weight:700;color:var(--ink);letter-spacing:.5px}
  .intro h1::after{content:"";display:block;width:90px;height:3px;background:var(--blue);margin:14px auto 22px}
  .intro p{font-size:14px;line-height:22px;text-align:left}

  /* services */
  .services{margin:0 110px;background:var(--blue);padding:70px 60px 46px;display:flex;flex-direction:column;gap:48px}
  .service{height:320px;background:var(--white);display:flex}
  .service.reverse{flex-direction:row-reverse}
  .service-media{width:430px;height:320px;flex:none}
  .service-body{flex:1;padding:56px 40px 0}
  .service.reverse .service-body{text-align:right}
  .service h2{font-size:21px;font-weight:600;color:var(--ink);text-transform:uppercase;margin-bottom:18px;display:flex;align-items:center;gap:10px;white-space:nowrap}
  .service.reverse h2{justify-content:flex-end}
  .service h2::before{content:"";width:5px;height:24px;background:var(--blue);flex:none}
  .service h2 em{font-style:normal;color:var(--blue)}
  .service p{font-size:14px;line-height:23px}

  .media-honest{background:linear-gradient(135deg,#eef2f5,#b9c6d2)}
  .media-malware{background:linear-gradient(135deg,#f6c935,#eaa91e)}
  .media-hardware{background:linear-gradient(135deg,#3f5a3a,#1e2a24)}
  .media-upgrades{background:linear-gradient(135deg,#a8764a,#5c3e27)}
  .media-migration{background:linear-gradient(135deg,#9aa9b6,#5d6d7b)}
  .media-rescue{background:linear-gradient(135deg,#e6e6e6,#8e8e8e)}
  .media-tune{background:linear-gradient(135deg,#6aa8dc,#24507e)}
  .media-install{background:linear-gradient(135deg,#f0ece6,#9c8a74)}
  .media-remote{background:linear-gradient(135deg,#3ab3d8,#1a5f8e)}

  /* map */
  .map{position:absolute;left:0;top:4270px;width:1200px;height:380px;background:linear-gradient(180deg,#eef0ec,#dfe4dd)}
  .map-pin{position:absolute;left:580px;top:150px;width:40px;height:56px;fill:var(--blue)}

  /* footer */
  .footer{position:absolute;left:0;top:4650px;width:1200px;height:278px;background:var(--footer);display:flex;padding:70px 80px 0;color:#bdbdbd}
  .footer .brand{color:var(--white);align-self:flex-start}
  .footer-contact{margin-left:130px;font-size:14px;line-height:30px}
  .footer-contact h3{color:var(--blue);font-size:15px;font-weight:700;margin-bottom:8px}
  .footer-contact span{display:flex;align-items:center;gap:10px}
  .footer-contact svg{width:16px;height:16px;fill:var(--blue)}
  .footer-meta{margin-left:auto;display:flex;align-items:flex-start;gap:14px;font-size:13px;padding-top:40px}
  .social{width:30px;height:30px;border-radius:50%;background:var(--white)}
  .footer-meta small{margin-left:16px;line-height:30px;font-size:13px}
</style>
</head>
<body>

<header class="topbar">
  <div class="brand"><span class="brand-dot"></span>NORVALE TECH</div>
  <div class="topbar-contact">
    <span><svg viewBox="0 0 24 24"><path d="M6.6 10.8a15.1 15.1 0 0 0 6.6 6.6l2.2-2.2a1 1 0 0 1 1-.25 11.4 11.4 0 0 0 3.6.57 1 1 0 0 1 1 1V20a1 1 0 0 1-1 1A17 17 0 0 1 3 4a1 1 0 0 1 1-1h3.5a1 1 0 0 1 1 1c0 1.25.2 2.45.57 3.57a1 1 0 0 1-.25 1z"/></svg>555 - 310 - 2468</span>
    <span><svg viewBox="0 0 24 24"><path d="M2 5h20v14H2zm2 2v.5l8 5 8-5V7l-8 5z"/></svg>info@norvaletech.com</span>
  </div>
</header>

<section class="hero">
  <ul class="hero-menu">
    <li>Buy</li><li>Repair</li><li>Service</li><li>Upgrade</li><li>Maintenace PC &amp; Laptop</li>
  </ul>
  <div class="hero-photo" role="img" aria-label="Technician repairing an open desktop computer"></div>
</section>

<section class="intro">
  <h1>LOREM IPSUM DUMMY TEXT PRINTING</h1>
  <p>Lorem ipsum is simply dummy text of the printing and typesetting industry. Lorem ipsum has been the industry's standard dummy text ever since the 1500s, when an unknown printer took a galley of type and scrambled it to make a type specimen book. It has survived not only five centuries, but also the leap into electronic typesetting, remaining essentially unchanged.</p>
</section>

<section class="services">
  <article class="service">
    <div class="service-media media-honest" role="img" aria-label="Smiling technician at a desk"></div>
    <div class="service-body"><h2><em>Honest</em> Service</h2><p>Our certified technicians won't sell or overcharge. We analyze the problem first, explain your options in plain words and only repair what really needs fixing, so you leave with a working machine and a fair bill.</p></div>
  </article>
  <article class="service reverse">
    <div class="service-media media-malware" role="img" aria-label="Illustration of a monitor with a virus warning"></div>
    <div class="service-body"><h2><em>Malware/Virus</em> Removal</h2><p>Infections can come from many places and sometimes without you knowing. We clean out viruses, spyware and adware, restore your settings and harden the system so it keeps running safe and fast after you pick it up.</p></div>
  </article>
  <article class="service">
    <div class="service-media media-hardware" role="img" aria-label="Close-up of a computer motherboard"></div>
    <div class="service-body"><h2><em>PC/Laptop</em> Hardware Repair</h2><p>From screens and keyboards to power jacks and fans, we find exactly which part of your computer is failing, order the right replacement and install it with care so your desktop or laptop works like new.</p></div>
  </article>
  <article class="service reverse">
    <div class="service-media media-upgrades" role="img" aria-label="Laptop showing a software update on a wooden desk"></div>
    <div class="service-body"><h2><em>Computer</em> Upgrades</h2><p>A new video card to play the latest games, more memory for heavy multitasking or a fast solid state drive to boot in seconds, we pick the parts that fit your budget and install them for you.</p></div>
  </article>
  <article class="service">
    <div class="service-media media-migration" role="img" aria-label="Illustration of data moving between two drives"></div>
    <div class="service-body"><h2><em>Data</em> Migration</h2><p>We can make your new computer feel like an old friend. Transfer all your files, photos, bookmarks, email accounts and program settings so everything is right where you left them.</p></div>
  </article>
  <article class="service reverse">
    <div class="service-media media-rescue" role="img" aria-label="External hard drive connected to a laptop"></div>
    <div class="service-body"><h2><em>Data</em> Rescue</h2><p>Hard drive failed? Files deleted by mistake? Don't panic. In many cases we can recover the photos, documents and projects that matter most, and we will tell you honestly before any charges apply.</p></div>
  </article>
  <article class="service">
    <div class="service-media media-tune" role="img" aria-label="Hands on a laptop with a remove button on screen"></div>
    <div class="service-body"><h2><em>Tune</em> Ups</h2><p>Over time, systems can get bogged down by startup programs and leftover clutter. We clear it out, update drivers and check the hardware so your computer runs at its best performance again.</p></div>
  </article>
  <article class="service reverse">
    <div class="service-media media-install" role="img" aria-label="Technician setting up a computer in a home"></div>
    <div class="service-body"><h2><em>In-Home</em> Installation</h2><p>All our services come with pick up and drop off. We can also come to your home or office to set up wireless networking, printers, cables and controllers so you don't have to do it yourself.</p></div>
  </article>
  <article class="service">
    <div class="service-media media-remote" role="img" aria-label="Illustration of a laptop connected for remote support"></div>
    <div class="service-body"><h2><em>Remote</em> Support</h2><p>Small problems shouldn't cost an evening. With your permission we connect securely to your computer, fix the issue while you watch and answer your questions without you ever leaving your desk.</p></div>
  </article>
</section>

<section class="map" role="img" aria-label="Street map showing the workshop location">
  <svg class="map-pin" viewBox="0 0 24 34"><path d="M12 0a12 12 0 0 0-12 12c0 9 12 22 12 22s12-13 12-22A12 12 0 0 0 12 0zm0 17a5 5 0 1 1 0-10 5 5 0 0 1 0 10z"/></svg>
</section>

<footer class="footer">
  <div class="brand"><span class="brand-dot"></span>NORVALE TECH</div>
  <div class="footer-contact">
    <h3>CONTACT INFO</h3>
    <span><svg viewBox="0 0 24 24"><path d="M6.6 10.8a15.1 15.1 0 0 0 6.6 6.6l2.2-2.2a1 1 0 0 1 1-.25 11.4 11.4 0 0 0 3.6.57 1 1 0 0 1 1 1V20a1 1 0 0 1-1 1A17 17 0 0 1 3 4a1 1 0 0 1 1-1h3.5a1 1 0 0 1 1 1c0 1.25.2 2.45.57 3.57a1 1 0 0 1-.25 1z"/></svg>555 - 310 - 2468</span>
    <span><svg viewBox="0 0 24 24"><path d="M2 5h20v14H2zm2 2v.5l8 5 8-5V7l-8 5z"/></svg>info@norvaletech.com</span>
  </div>
  <div class="footer-meta">
    <span class="social"></span><span class="social"></span><span class="social"></span>
    <small>© 2018 All Rights Reserved</small>
  </div>
</footer>

</body>
</html>
```